KORVAL Student Exchange needs a brochure design

I need a brochure design for KORVAL Student Exchange based in Auckland, New Zealand. I am responsible for outbound exchanges where I recruit local students from around New Zealand between the ages of 15 and 18 who are interested in going on an exchange overseas. Students can select from 12 different countries including America, France, Italy, the Netherlands, Spain, Ireland, Germany, Brazil Japan, and Argentina and choose the programme length from 3 months to an academic year (although we offer shorter programmes for some countries). I would like to attract students who are keen to learn about other cultures and experience something completely different to home. I would like to see vibrant colours and images that coveys fun, youthfulness and adventure.
Updates

Hi,

I have added pics and content for your viewing. 

Thanks.

Tessa

Hi,

Could I request that the designs are done on a tri-fold brochure

Also, I would like to see vibrant colours. So far, I have seen colours matching the logo (which is ok)  but I want to try and move away from that and start something fresh. Please look at the booklet and fee sheet which I have uploaded for ideas. 

I am wondering whether there is too much writing to fit on a tri fold brochure...
If you are having problems fitting everything in, please let me know.

I think the testimonial section could use up 2 spaces on the brochure. 

Target Market(s)

I would like to target teenagers who are interested in other cultures and want to enhance their language learning

Industry/Entity Type

Learn

Font styles to use
Serif
Sans Serif
Decorative

```html
<!DOCTYPE html>
<html lang="en">
<head>
<meta charset="utf-8">
<title>KORVAL Student Exchange – Brochure Inside Spread</title>
<link rel="stylesheet" href="https://fonts.googleapis.com/css2?family=Bebas+Neue&family=Lato:wght@400;700&display=swap">
<style>
  :root {
    --panel-top: #e5285a;
    --panel-mid: #b8467f;
    --panel-bottom: #7c4fa3;
    --heading-purple: #5e2f91;
    --headline-purple: #6b4b9e;
    --body-grey: #5a5a5a;
    --accent-green: #138a48;
    --sky-top: #7fa9d8;
    --sky-bottom: #e7eef7;
    --paper: #ffffff;
    --paper-shade: #e9e9ec;
    --blob-magenta: #d0177a;
    --blob-red: #e8322d;
    --blob-orange: #e8742a;
    --blob-blue: #1f6fc0;
    --blob-navy: #253e8a;
    --blob-green: #8cc63f;
    --blob-purple: #6a3c96;
  }
  * { margin: 0; padding: 0; box-sizing: border-box; }
  html, body { width: 1200px; height: 850px; overflow: hidden; background: var(--paper); }
  .spread {
    position: relative;
    width: 1200px;
    height: 850px;
    overflow: hidden;
    background: radial-gradient(ellipse at 60% 95%, var(--paper-shade) 0%, var(--paper) 65%);
    font-family: 'Lato', sans-serif;
  }
  .artwork { position: absolute; inset: 0; width: 1200px; height: 850px; }
  .headline {
    position: absolute;
    left: 420px; top: 18px;
    font-family: 'Bebas Neue', sans-serif;
    font-size: 44px;
    line-height: 38px;
    color: var(--headline-purple);
    letter-spacing: 0.3px;
  }
  .column { position: absolute; }
  .column h2 {
    font-family: 'Bebas Neue', sans-serif;
    font-weight: 400;
    text-align: center;
    letter-spacing: 0.3px;
  }
  .column p {
    font-size: 13.2px;
    line-height: 18.8px;
    text-align: justify;
    text-align-last: center;
  }
  .column--intro { left: 33px; top: 143px; width: 317px; color: #fff; }
  .column--intro h2 { font-size: 38px; line-height: 40px; margin-bottom: 10px; }
  .column--intro p { color: #fff; }
  .column--centre { left: 445px; top: 274px; width: 315px; }
  .column--right { left: 826px; top: 274px; width: 315px; }
  .column--centre h2, .column--right h2 { font-size: 35px; line-height: 38px; color: var(--heading-purple); margin-bottom: 20px; }
  .column--centre p, .column--right p { color: var(--body-grey); }
  .column--centre p + p { margin-top: 18px; }
  .highlight { color: var(--accent-green); }
</style>
</head>
<body>
<main class="spread">
  <svg class="artwork" viewBox="0 0 1200 850" aria-hidden="false">
    <defs>
      <linearGradient id="panelGradient" x1="0" y1="0" x2="0" y2="1">
        <stop offset="0" stop-color="var(--panel-top)"/>
        <stop offset="0.5" stop-color="var(--panel-mid)"/>
        <stop offset="1" stop-color="var(--panel-bottom)"/>
      </linearGradient>
      <linearGradient id="skyGradient" x1="0" y1="0" x2="0" y2="1">
        <stop offset="0" stop-color="var(--sky-top)"/>
        <stop offset="1" stop-color="var(--sky-bottom)"/>
      </linearGradient>
      <linearGradient id="studentsGradient" x1="0" y1="0" x2="1" y2="1">
        <stop offset="0" stop-color="#c9a58a"/>
        <stop offset="0.6" stop-color="#8a6a55"/>
        <stop offset="1" stop-color="#3d5a3a"/>
      </linearGradient>
      <linearGradient id="flagsGradient" x1="0" y1="0" x2="1" y2="1">
        <stop offset="0" stop-color="#6f9fd6"/>
        <stop offset="0.5" stop-color="#a8b6c8"/>
        <stop offset="1" stop-color="#b23a3a"/>
      </linearGradient>
    </defs>

    <!-- top sky photograph band -->
    <polygon class="photo photo--friends" role="img" aria-label="Photo of a smiling group of young friends posing against a bright blue sky"
      points="0,0 1200,0 1200,10 800,200" fill="url(#skyGradient)"/>
    <rect class="photo photo--friends-group" role="img" aria-label="Group of five smiling young friends" x="680" y="5" width="215" height="190" fill="#c9a08c" opacity="0.55"/>
    <polygon points="800,200 1200,10 1200,120" fill="var(--paper)"/>

    <!-- top left and top right decorative blobs -->
    <path class="blob" d="M40 0 C70 40 130 45 170 20 C200 45 260 70 300 40 L320 0 Z" fill="var(--blob-purple)" opacity="0.8"/>
    <path class="blob" d="M900 160 C930 120 990 110 1040 135 C1080 90 1150 70 1200 95 L1200 120 C1130 150 1080 175 1020 170 C980 150 940 165 900 160 Z" fill="var(--blob-green)"/>
    <path class="blob" d="M1000 160 C1020 120 1080 95 1130 100 C1170 80 1200 75 1200 75 L1200 125 C1140 160 1080 175 1040 170 Z" fill="var(--blob-blue)"/>
    <path class="blob" d="M940 135 C980 90 1050 70 1110 60 C1160 40 1200 35 1200 35 L1200 70 C1130 85 1060 110 1000 140 Z" fill="var(--blob-navy)" opacity="0.85"/>
    <path class="blob" d="M905 160 C925 140 960 135 990 148 L960 160 Z" fill="var(--blob-red)" opacity="0.9"/>

    <!-- left panel -->
    <polygon class="panel panel--intro" points="0,5 400,100 400,715 0,495" fill="url(#panelGradient)"/>

    <!-- bottom left students photograph -->
    <polygon points="0,500 400,720 470,850 0,850" fill="var(--paper)"/>
    <polygon class="photo photo--students" role="img" aria-label="Photo of excited teenage students looking at a tablet together"
      points="0,525 470,850 0,850" fill="url(#studentsGradient)"/>
    <path class="blob" d="M0 470 C40 490 80 510 110 530 C80 540 40 535 0 520 Z" fill="var(--blob-navy)" opacity="0.7"/>
    <path class="blob" d="M270 690 C300 660 360 655 400 680 C420 700 410 730 390 740 Z" fill="var(--blob-purple)" opacity="0.75"/>
    <path class="blob" d="M395 715 C420 720 450 735 460 760 L440 790 Z" fill="var(--blob-green)" opacity="0.8"/>

    <!-- bottom right flags photograph -->
    <polygon class="photo photo--flags" role="img" aria-label="Photo of international flags on flagpoles against a blue sky"
      points="510,850 1200,625 1200,850" fill="url(#flagsGradient)"/>
    <path class="blob" d="M460 850 C460 760 520 700 600 705 C680 710 720 760 800 720 C760 780 640 800 600 850 Z" fill="var(--blob-magenta)"/>
    <path class="blob" d="M540 850 C560 790 620 760 700 770 C640 800 600 830 590 850 Z" fill="var(--blob-red)" opacity="0.85"/>
    <path class="blob" d="M850 700 C850 650 890 620 940 625 C980 630 990 660 960 680 Z" fill="var(--blob-blue)" opacity="0.9"/>
    <path class="blob" d="M900 690 C960 650 1040 640 1100 625 C1140 615 1170 600 1200 590 L1200 625 C1100 660 1000 690 900 690 Z" fill="var(--blob-purple)" opacity="0.85"/>
    <path class="blob" d="M1090 630 C1110 595 1140 570 1165 575 C1180 590 1180 615 1175 635 Z" fill="var(--blob-orange)"/>
    <path class="arc" d="M640 850 C780 780 960 760 1200 780" fill="none" stroke="#f0a020" stroke-width="6"/>
    <path class="arc" d="M900 830 C1000 790 1100 760 1200 750" fill="none" stroke="#fff" stroke-width="5" stroke-dasharray="28 16"/>
  </svg>

  <h1 class="headline">It's time&nbsp; to make<br>new friends</h1>

  <section class="column column--intro">
    <h2>Lorem ipsum dolor</h2>
    <p>consectetur adipiscing elit. Mauris feugiat ante a augue vestibulum, et ultrices massa congue. Vestibulum arcu mauris, interdum convallis placerat id, pretium vitae diam. Maecenas vel viverra elit, eu bibendum lorem. Pellentesque habitant morbi tristique senectus et netus et malesuada fames ac turpis egestas. Duis quis elementum urna. Sed ac diam aliquet, suscipit sapien eleifend, tempus augue. Etiam sagittis, nulla nec imperdiet luctus, tortor libero commodo nibh, ut convallis purus arcu non odio. Donec a ipsum ac urna dapibus luctus. Proin dignissim sollicitudin semper. Quisque fermentum dapibus scelerisque.</p>
  </section>

  <section class="column column--centre">
    <h2>Curabitur accumsan quis</h2>
    <p>Aenean pulvinar nisi mi, ultrices pellentesque purus dictum eu. Vestibulum varius ante in nisi vestibulum, vel adipiscing tellus placerat. Nullam vehicula, orci sed ultrices suscipit, neque tortor egestas nunc, id ultrices mauris velit et mauris. Fusce nec scelerisque ante. Aenean tempor luctus tincidunt. Duis cursus interdum dignissim. Aenean sagittis urna volutpat quam varius vulputate.</p>
    <p>Aenean feugiat sit amet velit eu mattis. Etiam sit amet ligula ligula. Mauris quis ligula bibendum sapien aliquam gravida vitae id arcu. Aliquam tortor nibh, iaculis sit amet suscipit eu, vestibulum vitae metus. Pellentesque eget convallis elit. Nam sit amet dapibus nulla. In hac habitasse platea dictumst.</p>
  </section>

  <section class="column column--right">
    <h2>Nin faucibus.</h2>
    <p>&nbsp;Nullam lorem est, tincidunt vel tincidunt a, molestie a mauris. Curabitur accumsan quis magna vehicula dignissim. Pellentesque varius felis at nisl ultricies tempor at at nulla. Fusce eget massa quis leo laoreet elementum vitae eget dui. Cras tristique ultricies gravida. Duis tortor nisi, tristique ac orci ut, dictum pellentesque elit. Quisque sed blandit mi, vitae ornare mi. In hac habitasse platea dictumst. Etiam non tortor porttitor, lacinia neque vitae, feugiat diam. Praesent suscipit, ipsum non <span class="highlight">condimentum mattis, mi diam convallis dui, sed porta felis neque volutpat quam</span>.</p>
  </section>
</main>
</body>
</html>
```